36" inch (height) x 96" inch (width) Banner for Baseball Field

Hello. This project is an advertisement that will be printed onto a 3 foot by 8 foot full color banner and placed at little league fields in Southern California. A theme of the banner can be baseball. The company is my law office practicing Estate Planning and Tax Law. I am uploading the current business card, which has the logo, website, and telephone number. You can also pull images from www.rkpembrove.com I would like the banner to be a fun design that incorporates baseball somehow, but draws attention to my law and tax office, and my website. Please be creative, and have fun with it. The colors of my practice are included in the logo. At the bottom, it should say "Attorney Advertisement," but this can be in very small font in the bottom right or left corner.

Target Market(s)

Youth Baseball Fans

Industry/Entity Type

Law; Accounting

Colors

Designer to choose colors to be used in the design.

Requirements
Must have
• My telephone number. My website.
Nice to have
• Would like to see "Estate Planning" and "Tax Law and Preparation" Would also like to see "Attorney" and "CPA" or "Certified Public Accountant" prominently diplayed

```html
<!DOCTYPE html>
<html lang="en">
<head>
<meta charset="utf-8">
<title>RK Pembrove – Field Banner</title>
<link rel="stylesheet" href="https://fonts.googleapis.com/css2?family=Cinzel:wght@500;600&family=Montserrat:wght@500;600;700;800&display=swap">
<style>
  :root {
    --brand-blue: #1a96d4;
    --brand-grey: #939598;
    --phone-grey: #8a8d90;
    --ink: #000000;
    --paper: #ffffff;
    --stage: #c3c3c3;
  }
  * { margin: 0; padding: 0; box-sizing: border-box; }
  html, body {
    width: 800px; height: 1200px; overflow: hidden;
    background: var(--stage);
  }
  .banner {
    position: absolute; left: 20px; top: 457px;
    width: 760px; height: 285px;
    background: var(--ink);
    overflow: hidden;
    box-shadow: 0 6px 10px rgba(0,0,0,0.25);
  }
  .banner-shapes { position: absolute; inset: 0; width: 100%; height: 100%; }
  .headline {
    position: absolute; left: 40px;
    font-family: "Cinzel", serif; font-weight: 500;
    font-size: 45px; line-height: 1; letter-spacing: 0.5px;
  }
  .headline--estate { top: 28px; color: var(--brand-blue); }
  .headline--planning { top: 69px; color: var(--paper); }
  .headline-divider {
    position: absolute; left: 302px; top: 68px;
    width: 2px; height: 44px; background: var(--brand-blue);
  }
  .service {
    position: absolute; left: 314px;
    font-family: "Montserrat", sans-serif; line-height: 1;
    font-size: 22px;
  }
  .service--tax { top: 74px; color: var(--paper); font-weight: 500; letter-spacing: 0.5px; }
  .service--prep { top: 94px; color: var(--brand-grey); font-weight: 800; }
  .band-text {
    position: absolute; display: flex; align-items: center;
    font-family: "Montserrat", sans-serif; line-height: 1;
  }
  .band-text--cpa {
    left: 40px; top: 130px; height: 45px;
    font-size: 25.5px; font-weight: 800; color: var(--paper); letter-spacing: 0.2px;
  }
  .band-text--name {
    left: 38px; top: 175px; height: 50px;
    font-size: 21px; font-weight: 700; color: var(--paper);
  }
  .band-text--attorney {
    left: 324px; top: 176px; height: 50px;
    font-size: 27px; font-weight: 700; color: var(--ink); letter-spacing: 0.5px;
  }
  .contact {
    position: absolute; top: 225px; height: 60px;
    display: flex; align-items: center;
    font-family: "Montserrat", sans-serif; line-height: 1;
  }
  .contact--web {
    left: 36px; font-size: 14.5px; font-weight: 500; color: var(--ink); letter-spacing: 1.6px;
  }
  .contact--web .domain { color: var(--brand-blue); font-weight: 700; }
  .contact--phone {
    left: 244px; font-size: 25px; font-weight: 800; color: var(--phone-grey); gap: 3px;
  }
  .phone-icon { width: 21px; height: 21px; }
  .firm-mark {
    position: absolute; left: 619px; top: 114px;
    width: 50px; height: 50px; border-radius: 50%;
    border: 3px solid var(--brand-blue);
  }
  .firm-name {
    position: absolute; left: 544px; width: 200px; top: 186px;
    text-align: center;
    font-family: "Cinzel", serif; font-weight: 500;
    font-size: 21px; color: var(--brand-blue); line-height: 1;
  }
  .ad-notice {
    position: absolute; left: 544px; width: 200px; top: 242px;
    text-align: center;
    font-family: "Montserrat", sans-serif; font-weight: 600;
    font-size: 8.5px; letter-spacing: 2.2px; color: var(--paper); line-height: 1;
  }
</style>
</head>
<body>
  <div class="banner">
    <svg class="banner-shapes" viewBox="0 0 1372 514" preserveAspectRatio="none" aria-hidden="true">
      <rect class="panel-white" x="0" y="315" width="1372" height="199" fill="var(--paper)"/>
      <rect class="band-blue" x="0" y="234" width="1372" height="81" fill="var(--brand-blue)"/>
      <path class="band-grey" d="M0 315 L560 315 C538 320 527 342 517 370 C507 398 492 407 470 407 L0 407 Z" fill="var(--brand-grey)"/>
      <path class="swoosh-blue" d="M1225 42 C1060 75 915 180 900 330 C892 420 905 480 925 514 L1372 514 L1372 42 Z" fill="var(--brand-blue)"/>
      <path class="swoosh-black-gap" d="M1372 50 C1160 30 1000 150 950 320 C940 400 960 470 985 514 L1372 514 Z" fill="var(--ink)"/>
      <path class="swoosh-grey" d="M1372 57 C1150 35 990 160 962 330 C956 370 960 400 968 420 L1372 420 Z" fill="var(--brand-grey)"/>
      <path class="seal-black" d="M1372 152 C1170 100 1010 190 980 330 C965 400 978 460 1000 514 L1372 514 Z" fill="var(--ink)"/>
    </svg>

    <div class="headline headline--estate">ESTATE</div>
    <div class="headline headline--planning">PLANNING</div>
    <div class="headline-divider"></div>
    <div class="service service--tax">TAX LAW &amp;</div>
    <div class="service service--prep">PREPARATION</div>

    <div class="band-text band-text--cpa">CERTIFIED PUBLIC ACCOUNTANT</div>
    <div class="band-text band-text--name">Robert K. Pembrove</div>
    <div class="band-text band-text--attorney">ATTORNEY</div>

    <div class="contact contact--web">www.<span class="domain">rkpembrove</span>.com</div>
    <div class="contact contact--phone">
      <svg class="phone-icon" viewBox="0 0 24 24" aria-hidden="true">
        <circle cx="12" cy="12" r="12" fill="var(--brand-blue)"/>
        <path d="M8.2 5.5c.5-.3 1.1-.2 1.4.3l1.3 2.2c.3.5.2 1.1-.2 1.4l-1 .8c.6 1.6 1.8 2.9 3.4 3.7l.9-1c.4-.4 1-.5 1.4-.2l2.2 1.4c.5.3.6 1 .3 1.4l-.9 1.3c-.5.7-1.4 1-2.2.7-3.5-1.3-6.2-4-7.4-7.6-.3-.8 0-1.7.7-2.2z" fill="var(--paper)"/>
      </svg>
      <span>(805) 555-0148</span>
    </div>

    <div class="firm-mark"></div>
    <div class="firm-name">RK PEMBROVE</div>
    <div class="ad-notice">ATTORNEY ADVERTISEMENT</div>
  </div>
</body>
</html>
```